Brightwire Hollow Business cards

one side I would like my logo (uploaded) and the other side I want my details. I'm an electrician in sydney. The logo side I'm happy with just a white background and our logo in the middle.

Details for other side
24/7 Sydney Electrician
Marcus Pell
0431 587 219
marcus@brightwirehollow.com.au
brightwirehollow.com.au
icons for facebook, instagram, linked in

Industry/Entity Type

electrician

Contact Information for Business Card

company info

```html
<!DOCTYPE html>
<html lang="en">
<head>
<meta charset="utf-8">
<title>Brightwire Hollow – Business Cards</title>
<link href="https://fonts.googleapis.com/css2?family=Montserrat:wght@600;700&display=swap" rel="stylesheet">
<style>
  :root {
    --backdrop: #b3b3b3;
    --card: #ffffff;
    --ink: #111111;
    --accent: #d9261c;
  }
  * { margin: 0; padding: 0; box-sizing: border-box; }
  html, body {
    width: 1200px; height: 1200px; overflow: hidden;
    background: var(--backdrop);
    font-family: "Montserrat", sans-serif;
    color: var(--ink);
  }
  .card {
    position: absolute;
    left: 242px; width: 715px; height: 462px;
    background: var(--card);
  }
  .card--front { top: 86px; }
  .card--back { top: 652px; }

  .brand-name {
    position: absolute; left: 0; right: 0; top: 212px;
    text-align: center;
    font-weight: 700; font-size: 34px;
    color: var(--accent);
    letter-spacing: 0.01em;
  }

  .holder-name {
    position: absolute; left: 0; right: 0; top: 38px;
    text-align: center;
    font-weight: 700; font-size: 27px; letter-spacing: 0.02em;
    text-transform: uppercase;
  }
  .holder-rule {
    position: absolute; left: 267px; width: 181px; top: 79px;
    height: 5px; border-radius: 3px; background: var(--accent);
  }

  .contact-icon {
    position: absolute; left: 348px; width: 19px; height: 19px;
  }
  .contact-text {
    position: absolute; left: 0; right: 0;
    text-align: center;
    font-weight: 600; font-size: 19px; letter-spacing: 0.04em;
    line-height: 1;
  }
  .icon-phone { top: 119px; }
  .text-phone { top: 147px; }
  .icon-mail { top: 189px; }
  .text-mail { top: 214px; }
  .icon-web { top: 253px; }
  .text-web { top: 281px; }

  .social-row {
    position: absolute; left: 0; right: 0; top: 338px;
    display: flex; justify-content: center; gap: 19px;
  }
  .social-dot {
    width: 20px; height: 20px; border-radius: 50%;
    background: var(--accent);
  }

  .tagline {
    position: absolute; left: 0; right: 0; top: 396px;
    text-align: center;
    font-weight: 700; font-size: 17px; letter-spacing: 0.2em;
    text-transform: uppercase;
  }
</style>
</head>
<body>
  <section class="card card--front">
    <div class="brand-name">Brightwire Hollow</div>
  </section>

  <section class="card card--back">
    <h1 class="holder-name">Marcus Pell</h1>
    <div class="holder-rule"></div>

    <svg class="contact-icon icon-phone" viewBox="0 0 20 20" aria-hidden="true">
      <circle cx="10" cy="10" r="10" fill="var(--accent)"/>
      <path d="M7 5.2c.4-.3.9-.2 1.1.2l.9 1.7c.2.4.1.8-.2 1.1l-.6.5c.5 1.2 1.5 2.2 2.7 2.7l.5-.6c.3-.3.7-.4 1.1-.2l1.7.9c.4.2.5.7.2 1.1l-.6.9c-.4.5-1 .7-1.6.5C9.4 13.4 6.6 10.6 5.9 7.8c-.2-.6 0-1.2.5-1.6z" fill="#fff"/>
    </svg>
    <div class="contact-text text-phone">0431 587 219</div>

    <svg class="contact-icon icon-mail" viewBox="0 0 20 20" aria-hidden="true">
      <circle cx="10" cy="10" r="10" fill="var(--accent)"/>
      <rect x="4.5" y="6.2" width="11" height="7.6" rx="0.6" fill="#fff"/>
      <path d="M4.8 6.6 10 10.6l5.2-4M4.8 13.4l3.8-3.6M15.2 13.4l-3.8-3.6" stroke="var(--accent)" stroke-width="0.8" fill="none"/>
    </svg>
    <div class="contact-text text-mail">marcus@brightwirehollow.com.au</div>

    <svg class="contact-icon icon-web" viewBox="0 0 20 20" aria-hidden="true">
      <circle cx="10" cy="10" r="10" fill="var(--accent)"/>
      <g stroke="#fff" stroke-width="1.1" fill="none">
        <circle cx="10" cy="10" r="5.6"/>
        <ellipse cx="10" cy="10" rx="2.4" ry="5.6"/>
        <path d="M4.4 10h11.2"/>
      </g>
    </svg>
    <div class="contact-text text-web">brightwirehollow.com.au</div>

    <div class="social-row">
      <span class="social-dot" role="img" aria-label="Social profile link one"></span>
      <span class="social-dot" role="img" aria-label="Social profile link two"></span>
      <span class="social-dot" role="img" aria-label="Social profile link three"></span>
    </div>

    <div class="tagline">24/7 Sydney Electrician</div>
  </section>
</body>
</html>
```